Holvik Cabinets Quality Custom Built Kitchens, Vanity Units, Robes ect

Hi,
Was after a new design for our business cards,
we are a cabinet making business and pride ourselves in quality custom built Kitchens, Vanity units, robes ect.
we have been around for over 20 years and we are trying to modernize our card logo.
Looking for something eye catching, bold and exciting
family ran and operated business, we work with builders and also have a large private clientel.

Thanks

Industry/Entity Type

Business

Contact Information for Business Card

Holvik Cabinets

Font styles to use
Serif
Script

Requirements
Must have
• Corinne 0461735928 hvcabinets@mailvane.com
• Po Box 2786
• 5B Wattlebark Court Kestrel Vale Vic 3851
• Phone (03)59286417 Fax (03) 59286942
Nice to have
• Crafted Kitchens, Vanities & Robes Made to Measure

```html
<!DOCTYPE html>
<html lang="en">
<head>
<meta charset="utf-8">
<title>Holvik Cabinets – Business Card</title>
<link rel="stylesheet" href="https://fonts.googleapis.com/css2?family=Cinzel:wght@700&family=Montserrat:wght@400;500&display=swap">
<style>
  :root {
    --bg: #e6e3de;
    --card: #0d0d0d;
    --orange: #f39321;
    --copper: #c1732a;
    --tan: #c7a06f;
    --ink: #141414;
  }
  * { margin: 0; padding: 0; box-sizing: border-box; }
  html, body { width: 1200px; height: 1000px; overflow: hidden; background: var(--bg); }
  .sheet { position: relative; width: 1200px; height: 1000px; }
  .card {
    position: absolute; left: 237px; width: 726px; height: 425px;
    background: var(--card); overflow: hidden;
    box-shadow: 0 6px 18px rgba(0,0,0,0.25);
  }
  .card--back { top: 50px; }
  .card--front { top: 520px; }
  .card__shapes { position: absolute; inset: 0; }

  .brand { position: absolute; display: flex; align-items: center; gap: 16px; }
  .brand__mark { width: 30px; height: 30px; background: var(--orange); flex: none; }
  .brand__name {
    font-family: "Montserrat", sans-serif; font-weight: 500; color: var(--copper);
    line-height: 1; white-space: nowrap;
  }
  .brand__tagline {
    font-family: "Montserrat", sans-serif; font-weight: 400;
    white-space: nowrap; line-height: 1; color: var(--tan);
  }

  .card--back .brand { left: 0; right: 0; top: 172px; justify-content: center; }
  .card--back .brand__name { font-size: 44px; }
  .card--back .brand__tagline { font-size: 19px; margin-top: 12px; }

  .card--front .brand { left: 170px; top: 78px; }
  .card--front .brand__name { font-size: 38px; }
  .card--front .brand__tagline { font-size: 16px; margin-top: 10px; }

  .holder {
    position: absolute; left: 80px; width: 566px; top: 204px;
    text-align: center; font-family: "Cinzel", serif; font-weight: 700;
    font-size: 31px; line-height: 40px; color: var(--ink); letter-spacing: 1px;
  }
  .email {
    position: absolute; left: 80px; width: 566px; top: 263px; text-align: center;
    font-family: "Montserrat", sans-serif; font-size: 15px; color: var(--copper);
  }
  .postal {
    position: absolute; left: 34px; top: 357px; font-style: normal;
    font-family: "Montserrat", sans-serif; font-size: 15px; line-height: 21px; color: var(--copper);
  }
  .numbers {
    position: absolute; right: 28px; top: 334px; text-align: right;
    font-family: "Montserrat", sans-serif; font-size: 15px; line-height: 20px; color: var(--ink);
  }
</style>
</head>
<body>
<main class="sheet">

  <section class="card card--back" aria-label="Business card back">
    <div class="brand">
      <span class="brand__mark"></span>
      <div>
        <div class="brand__name">Holvik Cabinets</div>
        <div class="brand__tagline">Crafted Kitchens, Vanities &amp; Robes Made to Measure</div>
      </div>
    </div>
  </section>

  <section class="card card--front" aria-label="Business card front">
    <svg class="card__shapes" width="726" height="425" viewBox="0 0 726 425" aria-hidden="true">
      <rect x="60" y="185" width="600" height="77" fill="var(--copper)"/>
      <polygon points="726,100 726,425 400,425" fill="var(--copper)"/>
      <polygon points="0,0 62,0 140,78 40,178 0,138" fill="var(--tan)"/>
      <polygon points="0,105 42,63 158,178 0,336" fill="var(--orange)"/>
    </svg>

    <div class="brand">
      <span class="brand__mark"></span>
      <div>
        <div class="brand__name">Holvik Cabinets</div>
        <div class="brand__tagline">Crafted Kitchens, Vanities &amp; Robes Made to Measure</div>
      </div>
    </div>

    <div class="holder">Corinne</div>
    <div class="email">hvcabinets@mailvane.com</div>

    <address class="postal">
      Po Box 2786<br>
      5B Wattlebark Court Kestrel Vale Vic 3851
    </address>

    <div class="numbers">
      Mob: 0461 735 928<br>
      Phone: (03)59286417<br>
      Fax: (03) 59286942
    </div>
  </section>

</main>
</body>
</html>
```